Business card design for a world class martial arts and group fitness facility

We need a professional and eye catching design for a business card. The card will be used in networking as well as marketing.
We are a martial arts facility offering Taekwondo, Brazilian Jiu Jitsu, and group fitness. All of our programs are geared for kids and adults.
Our Taekwondo program is lead by a Hall of Fame instructor who was Instructor of the Year in 2015.
Our Brazilian Jiu Jitsu program is lead by a wold class instructor who is also a part of the renown Brazilian KLO team.
We offer 3 focused group fitness programs: Ridge kickboxing, Tandem Fitness, and The Quarry which are all lead by certified instructors in a small group setting.
Our facility is state of the art and has been recognized as such in nationally published magazines.
Our business is named The Forge which is the linear logo that is attached. This is the main logo. I also attached a circular logo we have used in some marketing material. Our Jiu Jitsu program is the KLO team logo. The Taekwondo program is the VORTEN Prime. It would be nice to somehow incorporate all 3 logos, but The Forge is most important.
We would like to use all 3 logos if possible but The Forge is the most important. We would like to have a place for a staff member's name while keeping the focus on the programs we offer.

```html
<!DOCTYPE html>
<html lang="en">
<head>
<meta charset="utf-8">
<title>The Forge – Business Card</title>
<link href="https://fonts.googleapis.com/css2?family=Lato:wght@400;700;900&display=swap" rel="stylesheet">
<style>
  :root {
    --page: #d6d6d6;
    --charcoal: #333333;
    --charcoal-deep: #262626;
    --steel-light: #5f5f5f;
    --steel-mid: #8c8c8c;
    --band-light: #dcdcdc;
    --ink: #111111;
    --forge-red: #e30613;
    --program-text: #cfcfcf;
    --white: #ffffff;
  }
  * { box-sizing: border-box; margin: 0; padding: 0; }
  html, body { width: 1200px; height: 830px; overflow: hidden; }
  body {
    background: var(--page);
    font-family: "Lato", sans-serif;
    position: relative;
  }
  .card {
    position: absolute;
    left: 280px;
    width: 640px;
    height: 366px;
    overflow: hidden;
    box-shadow: 0 6px 18px rgba(0,0,0,0.25);
  }

  /* Logo side */
  .card--logo {
    top: 24px;
    background: radial-gradient(ellipse at 50% 45%, var(--steel-mid) 0%, var(--steel-light) 80%);
    display: flex;
    align-items: center;
    justify-content: center;
  }
  .seal {
    width: 250px;
    height: 250px;
    border: 5px solid var(--charcoal-deep);
    border-radius: 50%;
    display: flex;
    align-items: center;
    justify-content: center;
  }
  .seal__name {
    font-weight: 900;
    font-size: 42px;
    color: var(--charcoal-deep);
    letter-spacing: 1px;
    white-space: nowrap;
  }

  /* Program side */
  .card--programs {
    top: 440px;
    background: var(--charcoal);
  }
  .light-band {
    position: absolute;
    left: 0;
    top: 44px;
    width: 400px;
    height: 126px;
    background: var(--band-light);
  }
  .light-band--edge {
    left: 590px;
    top: 150px;
    width: 50px;
    height: 66px;
  }
  .wordmark {
    position: absolute;
    left: 22px;
    top: 76px;
    font-weight: 900;
    font-size: 56px;
    line-height: 1;
    color: var(--ink);
    letter-spacing: 1px;
    text-transform: uppercase;
    white-space: nowrap;
  }
  .programs {
    position: absolute;
    left: 24px;
    top: 190px;
    list-style: none;
  }
  .programs__item {
    display: flex;
    align-items: center;
    gap: 14px;
    height: 40px;
    font-weight: 700;
    font-size: 19px;
    color: var(--program-text);
  }
  .programs__item::before {
    content: "";
    width: 10px;
    height: 26px;
    background: var(--forge-red);
    opacity: 0.8;
  }
  .partner-team {
    position: absolute;
    left: 236px;
    top: 276px;
    display: flex;
    align-items: center;
    gap: 8px;
    font-weight: 700;
    font-size: 15px;
    color: var(--white);
  }
  .partner-team__mark {
    width: 14px;
    height: 14px;
    background: var(--forge-red);
  }
  .contact-panel {
    position: absolute;
    left: 400px;
    top: 28px;
    width: 190px;
    height: 338px;
    background: var(--forge-red);
  }
  .team-badge {
    position: absolute;
    left: 30px;
    top: 20px;
    width: 130px;
    height: 130px;
    border-radius: 50%;
    background: #000;
    display: flex;
    align-items: center;
    justify-content: center;
    font-weight: 700;
    font-size: 30px;
    color: var(--white);
    letter-spacing: 2px;
  }
  .contact {
    position: absolute;
    left: 14px;
    right: 10px;
    top: 186px;
    font-style: normal;
    font-size: 12px;
    line-height: 22px;
    color: var(--white);
    white-space: nowrap;
  }
</style>
</head>
<body>
  <section class="card card--logo" aria-label="Card front">
    <div class="seal">
      <span class="seal__name">The Forge</span>
    </div>
  </section>

  <section class="card card--programs" aria-label="Card back">
    <div class="light-band"></div>
    <div class="light-band light-band--edge"></div>
    <h1 class="wordmark">The Forge</h1>
    <ul class="programs">
      <li class="programs__item">Ridge kickboxing</li>
      <li class="programs__item">Tandem Fitness</li>
      <li class="programs__item">The Quarry</li>
    </ul>
    <div class="partner-team">
      <span class="partner-team__mark"></span>
      <span>VORTEN Prime</span>
    </div>
    <div class="contact-panel">
      <div class="team-badge">KLO</div>
      <address class="contact">
        555 210 480217<br>
        1420 Anvil Rd, Denver, USA<br>
        hello@theforgegym.com<br>
        www.theforgegym.com
      </address>
    </div>
  </section>
</body>
</html>
```